Letterhead and Envelopes design using existing logo. Logo can be found at ridgemontcaldera.com

Use existing logo (attached) and incorporate in letterhead and envelope designs.

Current logo can be viewed at ridgemontcaldera.com the web site reflect various parent and sub companies. Please see attached as well.

Target Market(s)

Other oil and gas operators.

Industry/Entity Type

Oil And Gas

Font styles to use
Sans Serif

Colors

Designer to choose colors to be used in the design.

Requirements
Must have
• Current logo and address
Nice to have
• Modern, contemporary approach yet incorporate existing traditional design.
• After design is selected for Ridgemont Caldera Holdings I will use similar design for Royalties, Exploration, Energy and Farms with different color schemes.

```html
<!DOCTYPE html>
<html lang="en">
<head>
<meta charset="utf-8">
<title>Ridgemont Caldera Holdings – Stationery</title>
<link rel="stylesheet" href="https://fonts.googleapis.com/css2?family=Montserrat:wght@400;700&display=swap">
<style>
  :root {
    --backdrop: #d4d4d4;
    --paper: #ededed;
    --ink: #111111;
    --text-grey: #555555;
    --brand-green: #5e8c3a;
    --watermark: #dcdcdc;
    --rule: #9a9a9a;
    --flap: #1f2020;
  }
  * { margin: 0; padding: 0; box-sizing: border-box; }
  html, body { width: 1200px; height: 810px; overflow: hidden; }
  body {
    background: var(--backdrop);
    font-family: "Montserrat", Arial, sans-serif;
    position: relative;
  }
  .sheet { position: absolute; background: var(--paper); overflow: hidden; }

  .letterhead { left: 137px; top: 110px; width: 436px; height: 614px; }
  .envelope-back { left: 619px; top: 194px; width: 444px; height: 221px; }
  .envelope-front { left: 618px; top: 444px; width: 445px; height: 221px; }

  .brand { position: absolute; display: flex; align-items: center; gap: 8px; }
  .brand-dot { border-radius: 50%; background: var(--brand-green); flex: none; }
  .brand-name {
    color: var(--ink); font-weight: 700; text-transform: uppercase;
    line-height: 1.2; letter-spacing: 0.4px; white-space: nowrap;
  }
  .letterhead .brand { left: 38px; top: 46px; }
  .letterhead .brand-dot { width: 40px; height: 40px; }
  .letterhead .brand-name { font-size: 10.5px; }

  .contact {
    position: absolute; left: 295px; top: 46px; height: 56px;
    border-left: 1px solid var(--rule); padding-left: 9px;
    font-size: 8px; color: var(--text-grey); line-height: 10px;
    white-space: nowrap;
  }
  .contact .address { margin: 1px 0 8px; }
  .contact ul { list-style: none; }
  .contact li { display: flex; align-items: center; gap: 3px; height: 10.5px; }
  .contact svg { width: 7px; height: 7px; flex: none; }

  .watermark {
    position: absolute; left: 118px; top: 318px; width: 200px;
    text-align: center; color: var(--watermark); font-weight: 700;
    font-size: 22px; line-height: 1.15; text-transform: uppercase;
  }

  .band { position: absolute; left: 0; bottom: 0; width: 100%; display: block; }
  .letterhead .band { height: 10px; }
  .envelope-front .band { height: 9px; }

  .flap { position: absolute; left: 0; top: 0; width: 444px; height: 66px; display: block; }

  .envelope-front .brand { left: 24px; top: 32px; }
  .envelope-front .brand-dot { width: 30px; height: 30px; }
  .envelope-front .brand-name { font-size: 8px; }
  .return-address {
    position: absolute; left: 24px; top: 92px;
    font-size: 8px; line-height: 10px; color: var(--text-grey);
  }
</style>
</head>
<body>

<section class="sheet letterhead" aria-label="Letterhead">
  <div class="brand">
    <span class="brand-dot"></span>
    <span class="brand-name">Ridgemont<br>Caldera<br>Holdings</span>
  </div>

  <div class="contact">
    <p class="address">PO Box 318 Larkfield<br>North Dakota 58219</p>
    <ul>
      <li><svg viewBox="0 0 24 24"><path fill="var(--brand-green)" d="M6.6 10.8a15 15 0 0 0 6.6 6.6l2.2-2.2a1 1 0 0 1 1-.25 11.4 11.4 0 0 0 3.6.57 1 1 0 0 1 1 1V20a1 1 0 0 1-1 1A17 17 0 0 1 3 4a1 1 0 0 1 1-1h3.5a1 1 0 0 1 1 1c0 1.25.2 2.45.57 3.57a1 1 0 0 1-.25 1z"/></svg>701-555-0142</li>
      <li><svg viewBox="0 0 24 24"><rect x="2" y="5" width="20" height="14" fill="var(--brand-green)"/><path d="M3 6l9 7 9-7" fill="none" stroke="var(--paper)" stroke-width="2"/></svg>info@ridgemontcaldera.com</li>
      <li><svg viewBox="0 0 24 24"><circle cx="12" cy="12" r="10" fill="var(--brand-green)"/><path d="M2 12h20M12 2c3 3 3 17 0 20M12 2c-3 3-3 17 0 20" fill="none" stroke="var(--paper)" stroke-width="1.6"/></svg>www.ridgemontcaldera.com</li>
    </ul>
  </div>

  <p class="watermark">Ridgemont<br>Caldera<br>Holdings</p>

  <svg class="band" viewBox="0 0 436 10" preserveAspectRatio="none" aria-hidden="true">
    <polygon points="0,0 260,0 267,10 0,10" fill="var(--ink)"/>
    <polygon points="264,0 436,0 436,10 271,10" fill="var(--brand-green)"/>
  </svg>
</section>

<section class="sheet envelope-back" aria-label="Envelope, back with flap">
  <svg class="flap" viewBox="0 0 444 66" aria-hidden="true">
    <path d="M0,0 H444 L435,54 Q433,65 422,65 H22 Q11,65 9,54 Z" fill="var(--flap)"/>
  </svg>
</section>

<section class="sheet envelope-front" aria-label="Envelope, front">
  <div class="brand">
    <span class="brand-dot"></span>
    <span class="brand-name">Ridgemont<br>Caldera<br>Holdings</span>
  </div>
  <p class="return-address">PO Box 318 Larkfield<br>North Dakota 58219</p>
  <svg class="band" viewBox="0 0 445 9" preserveAspectRatio="none" aria-hidden="true">
    <polygon points="0,0 277,0 283,9 0,9" fill="var(--ink)"/>
    <polygon points="281,0 445,0 445,9 287,9" fill="var(--brand-green)"/>
  </svg>
</section>

</body>
</html>
```